standardize print collateral

we need help standardizing all print collateral and website. top priorities:

1. standardized case studies template
2. standardized marketing slicks template
3. standardized powerpoint template
Updates

Project Deadline Extended
Reason: We are extending the project to allow current design submissions to be tweaked while providing the opportunity for new designs to be submitted. We will need all 3 collateral designs submitted to make a final decision. Please note, these 3 designs should all look different, needless to say they should all compliment eachother. As for some direction, the powerpoint main color should not be yellow since yellow does not show up the same shade on any screen. The case study and marketing slicks will be printed and often sit next to our competitors marketing material - think high end product, technology, revolutionary, edgy, professional. The designs should compliment eachother and feel like the Brightfen Metrics brand (which you are determining) and should stand out professionally. We are open to introducing new colors into our brand, the only thing that must remain the same is our logo. Have fun, make it edgy, and keep it professional. Looking forward to seeing what you submit!

Target Market(s)

Property Casualty Insurance Companies: Executive level wording with actuarial credibility

Industry/Entity Type

Marketing

Requirements
Must have
• professional layout for existing collateral and 2-page marketing slicks. style guide/colors can be transferred to powerpoint. logo must stay; everything else (i.e. color, font, layout/structure etc.) is flexible. The three components should not looks the same, they should only compliment eachother.
Nice to have
• we are revolutionizing a conservative industry, so adequate level of edgy/advanced technology/impactful feel to layout
Should not have
• no need to stay within color constraints of yellow, but need to appropriately work well with the eagle head logo

```html
<!DOCTYPE html>
<html lang="en">
<head>
<meta charset="utf-8">
<title>Rapid Portfolio Analysis – Brightfen Metrics Flyer Set</title>
<link rel="stylesheet" href="https://fonts.googleapis.com/css2?family=Barlow:wght@300;400;600;700&family=Barlow+Semi+Condensed:wght@500;600;700&display=swap">
<style>
  :root {
    --backdrop: #8e8e8e;
    --paper: #ffffff;
    --gold: #f2b01e;
    --gold-dark: #e09a10;
    --ink: #1e1e1e;
    --ink-soft: #3b3b3b;
    --black: #0d0d0d;
    --good: #5bb75b;
    --warn: #f2c94c;
    --bad: #e0483e;
  }
  * { box-sizing: border-box; margin: 0; padding: 0; }
  html, body { width: 1200px; height: 900px; overflow: hidden; }
  body { background: var(--backdrop); font-family: "Barlow", Arial, sans-serif; color: var(--ink); position: relative; }

  /* Colour themes */
  .flyer--red {
    --head-a: #d41f26; --head-b: #5e0a0e;
    --tag-text: #8f0f16;
    --intro-bg: #ffffff; --intro-text: #1e1e1e;
    --tab-bg: #e2242b; --step-title: #1e1e1e;
    --panel-bg: #0d0d0d; --panel-text: #ffffff; --panel-caption: #e6e6e6;
    --foot-bg: #dc2128;
    --photo: linear-gradient(160deg, #e7eef3 0%, #b9c9d4 45%, #6f8594 100%);
  }
  .flyer--blue {
    --head-a: #1d5ca8; --head-b: #0a1526;
    --tag-text: #0e2f5c;
    --intro-bg: #141414; --intro-text: #f2f2f2;
    --tab-bg: #14a7e6; --step-title: #14a7e6;
    --panel-bg: #0d0d0d; --panel-text: #ffffff; --panel-caption: #e6e6e6;
    --foot-bg: #1aaeea;
    --photo: linear-gradient(160deg, #3a4d63 0%, #1c2838 100%);
  }
  .flyer--green {
    --head-a: #8cc63f; --head-b: #1f2a0e;
    --tag-text: #2f4a0c;
    --intro-bg: #262626; --intro-text: #f2f2f2;
    --tab-bg: #7dbb3c; --step-title: #4e7f1c;
    --panel-bg: #f6ecd2; --panel-text: #1e1e1e; --panel-caption: #2b2b2b;
    --foot-bg: #7dbb3c;
    --photo: linear-gradient(150deg, #4a5564 0%, #1b2230 60%, #0e121a 100%);
  }

  .flyer {
    position: absolute; width: 620px; height: 804px; background: var(--paper);
    box-shadow: 0 6px 18px rgba(0,0,0,.3); overflow: hidden;
    transform-origin: top left;
  }
  .flyer--blue  { left: 40px;  top: 150px; transform: scale(.85); }
  .flyer--green { left: 640px; top: 70px;  transform: scale(.85); }
  .flyer--red   { left: 290px; top: 48px;  z-index: 2; }

  .masthead {
    position: absolute; left: 0; top: 0; width: 100%; height: 90px;
    background: linear-gradient(90deg, var(--head-a) 0%, var(--head-b) 100%);
  }
  .masthead-title {
    position: absolute; left: 36px; top: 26px;
    font-weight: 300; font-size: 31px; color: #fff; letter-spacing: .2px;
  }
  .intro-field { position: absolute; left: 0; top: 90px; width: 100%; height: 194px; background: var(--intro-bg); }
  .tagline-bar {
    position: absolute; left: 0; top: 90px; width: 300px; height: 26px;
    background: linear-gradient(90deg, var(--gold-dark), var(--gold));
    font-family: "Barlow Semi Condensed", Arial, sans-serif; font-weight: 700;
    font-size: 15px; color: var(--tag-text); padding: 4px 0 0 36px;
  }
  .intro-text {
    position: absolute; left: 36px; top: 124px; width: 266px;
    font-size: 9.2px; line-height: 1.32; font-weight: 600; color: var(--intro-text);
  }
  .hero-photo { position: absolute; left: 310px; top: 90px; width: 310px; height: 178px; background: var(--photo); }

  .section-tab {
    position: absolute; left: 0; top: 294px; width: 180px; height: 24px;
    background: var(--tab-bg); color: #fff;
    font-family: "Barlow Semi Condensed", Arial, sans-serif; font-weight: 700;
    font-size: 14px; padding: 3px 0 0 36px;
  }
  .steps { position: absolute; left: 50px; top: 328px; width: 236px; }
  .step { margin-bottom: 10px; }
  .step-title {
    font-family: "Barlow Semi Condensed", Arial, sans-serif; font-weight: 700;
    font-size: 12.5px; color: var(--step-title); margin-bottom: 3px;
  }
  .step-body { font-size: 9px; line-height: 1.35; color: var(--ink-soft); }

  .monitor-panel {
    position: absolute; left: 300px; top: 276px; width: 300px; height: 334px;
    background: var(--panel-bg); padding: 12px 12px 0; color: var(--panel-text);
  }
  .panel-heading { font-family: "Barlow Semi Condensed", Arial, sans-serif; font-weight: 700; font-size: 12.5px; margin-bottom: 6px; }
  .portfolio-table { width: 100%; border-collapse: collapse; background: #fff; color: #222; font-size: 5.4px; text-align: center; }
  .portfolio-table th { background: #dde3ea; font-weight: 700; padding: 2px 1px; border: 1px solid #c6ccd4; }
  .portfolio-table td { padding: 1.6px 1px; border: 1px solid #e2e5ea; }
  .portfolio-table .good { background: var(--good); color: #fff; }
  .portfolio-table .warn { background: var(--warn); }
  .portfolio-table .bad { background: var(--bad); color: #fff; }
  .panel-caption { font-size: 8.4px; line-height: 1.35; margin: 6px 0 10px; color: var(--panel-caption); }
  .distribution-screen { width: 100%; height: 78px; background: linear-gradient(90deg, #3f8f3f 0%, #8cc46a 30%, #f0d35a 55%, #e3653f 80%, #b9322a 100%); }

  .report-band {
    position: absolute; left: 0; top: 620px; width: 100%; height: 30px; background: var(--black);
    font-family: "Barlow Semi Condensed", Arial, sans-serif; font-weight: 700;
    font-size: 14px; color: var(--gold); padding: 6px 0 0 40px;
  }
  .report-body {
    position: absolute; left: 0; top: 650px; width: 100%; height: 154px; background: var(--foot-bg);
    color: #fff; font-size: 10px; line-height: 1.4; padding: 14px 40px 0;
  }
</style>
</head>
<body>

  <article class="flyer flyer--blue">
    <header class="masthead"><h1 class="masthead-title">Rapid Portfolio Analysis</h1></header>
    <div class="intro-field"></div>
    <div class="tagline-bar">Winning Against Adverse Selection</div>
    <p class="intro-text">The property and casualty market is over-supplied with excess capacity, and current pricing methods are inconsistent and outdated. This leads to a considerable level of adverse selection within nearly every portfolio. Almost every insurer is attracting customers who are underpriced and losing business where they are overpriced. This invisible effect only surfaces after evidence of slowly deteriorating portfolio loss ratios, resulting in premium increases across the portfolio. These across-the-board premium increases exacerbate the problem by overpricing the most profitable customers and driving them into the arms of competitors.</p>
    <div class="hero-photo" role="img" aria-label="Photo of a business professional in a dark office setting"></div>
    <h2 class="section-tab">How does it work?</h2>
    <div class="steps">
      <section class="step"><h3 class="step-title">Detection: Is the portfolio priced correctly?</h3><p class="step-body">Quillon employs a regression method based on a technological breakthrough. It exposes pricing imbalances by commonly employed rating methods including the GLM. These pricing imbalances are the major drivers of adverse selection.</p></section>
      <section class="step"><h3 class="step-title">Measurement: How is the portfolio trending?</h3><p class="step-body">Quillon scores the two most important attributes of the portfolio: the adequacy of rates and the quality of the business on a progressive basis. In addition, Quillon projects the financial outcome of business as it is written with startling accuracy. Insurers are able to know significantly in advance of trends in their business.</p></section>
      <section class="step"><h3 class="step-title">Correction: How to address the issues?</h3><p class="step-body">Quillon provides an array of options for addressing any deterioration in the portfolio. These options range from specifically designed rate adjustments and underwriting strategies, to simple distribution management sales and profitability strategies.</p></section>
    </div>
    <h2 class="report-band">Let Brightfen Metrics Build Your Portfolio Analysis Report</h2>
    <p class="report-body">The report details your portfolio trends and identifies future unseen problems before they occur. The insight provided in the report exhibits what is actually going on in your portfolio. This likely includes adverse selection, impact of price changes with unintended consequences, and the emerging trends in the composition of the book. The analysis results not only reveal past trends, but also predict future impact.</p>
  </article>

  <article class="flyer flyer--green">
    <header class="masthead"><h1 class="masthead-title">Rapid Portfolio Analysis</h1></header>
    <div class="intro-field"></div>
    <div class="tagline-bar">Winning Against Adverse Selection</div>
    <p class="intro-text">The property and casualty market is over-supplied with excess capacity, and current pricing methods are inconsistent and outdated. This leads to a considerable level of adverse selection within nearly every portfolio. Almost every insurer is attracting customers who are underpriced and losing business where they are overpriced. This invisible effect only surfaces after evidence of slowly deteriorating portfolio loss ratios, resulting in premium increases across the portfolio. These across-the-board premium increases exacerbate the problem by overpricing the most profitable customers and driving them into the arms of competitors.</p>
    <div class="hero-photo" role="img" aria-label="Photo of a man touching glowing interface buttons on a glass screen"></div>
    <aside class="monitor-panel">
      <h3 class="panel-heading">Portfolio Monitoring</h3>
      <table class="portfolio-table">
        <thead><tr><th>Period</th><th>Exposure</th><th>Premium</th><th>Losses</th><th>Claims</th><th>Loss Ratio</th><th>Rate Index</th><th>Score</th></tr></thead>
        <tbody>
          <tr><td>2005 Q1</td><td>51,210</td><td>$6,140K</td><td>$3,510K</td><td>412</td><td>57.2%</td><td class="good">0.98</td><td class="good">312</td></tr>
          <tr><td>2005 Q2</td><td>52,034</td><td>$6,225K</td><td>$3,702K</td><td>428</td><td>59.5%</td><td class="good">0.97</td><td class="good">305</td></tr>
          <tr><td>2005 Q3</td><td>50,871</td><td>$6,102K</td><td>$3,880K</td><td>437</td><td>63.6%</td><td class="warn">1.02</td><td class="warn">288</td></tr>
          <tr><td>2005 Q4</td><td>49,662</td><td>$5,964K</td><td>$3,905K</td><td>441</td><td>65.5%</td><td class="warn">1.04</td><td class="warn">281</td></tr>
          <tr><td>2006 Q1</td><td>48,930</td><td>$5,880K</td><td>$4,012K</td><td>455</td><td>68.2%</td><td class="bad">1.08</td><td class="warn">274</td></tr>
          <tr><td>2006 Q2</td><td>47,515</td><td>$5,731K</td><td>$4,150K</td><td>463</td><td>72.4%</td><td class="bad">1.11</td><td class="bad">262</td></tr>
          <tr><td>2006 Q3</td><td>46,208</td><td>$5,604K</td><td>$4,233K</td><td>470</td><td>75.5%</td><td class="bad">1.13</td><td class="bad">255</td></tr>
          <tr><td>Total</td><td>346,430</td><td>$41,646K</td><td>$27,392K</td><td>3,106</td><td>65.8%</td><td>1.05</td><td>282</td></tr>
        </tbody>
      </table>
      <p class="panel-caption">Predict the future loss ratio of the business being written - both renewals and new business.</p>
      <h3 class="panel-heading">Distribution Monitoring</h3>
      <div class="distribution-screen" role="img" aria-label="Software screen of a distribution outlet grid with green, yellow and red performance cells"></div>
      <p class="panel-caption">Constantly track the quality and performance of individual distribution outlets based on the underwriting score of each policy</p>
    </aside>
    <h2 class="report-band">Let Brightfen Metrics Build Your Portfolio Analysis Report</h2>
    <p class="report-body">The report details your portfolio trends and identifies future unseen problems before they occur. The insight provided in the report exhibits what is actually going on in your portfolio. This likely includes adverse selection, impact of price changes with unintended consequences, and the emerging trends in the composition of the book. The analysis results not only reveal past trends, but also predict future impact.</p>
  </article>

  <article class="flyer flyer--red">
    <header class="masthead"><h1 class="masthead-title">Rapid Portfolio Analysis</h1></header>
    <div class="intro-field"></div>
    <div class="tagline-bar">Winning Against Adverse Selection</div>
    <p class="intro-text">The property and casualty market is over-supplied with excess capacity, and current pricing methods are inconsistent and outdated. This leads to a considerable level of adverse selection within nearly every portfolio. Almost every insurer is attracting customers who are underpriced and losing business where they are overpriced. This invisible effect only surfaces after evidence of slowly deteriorating portfolio loss ratios, resulting in premium increases across the portfolio. These across-the-board premium increases exacerbate the problem by overpricing the most profitable customers and driving them into the arms of competitors.</p>
    <div class="hero-photo" role="img" aria-label="Photo of a businessman with a rolling case walking through a bright airport terminal"></div>
    <h2 class="section-tab">How does it work?</h2>
    <div class="steps">
      <section class="step"><h3 class="step-title">Detection: Is the portfolio priced correctly?</h3><p class="step-body">Quillon employs a regression method based on a technological breakthrough. It exposes pricing imbalances by commonly employed rating methods including the GLM. These pricing imbalances are the major drivers of adverse selection.</p></section>
      <section class="step"><h3 class="step-title">Measurement: How is the portfolio trending?</h3><p class="step-body">Quillon scores the two most important attributes of the portfolio: the adequacy of rates and the quality of the business on a progressive basis. In addition, Quillon projects the financial outcome of business as it is written with startling accuracy. Insurers are able to know significantly in advance of trends in their business.</p></section>
      <section class="step"><h3 class="step-title">Correction: How to address the issues?</h3><p class="step-body">Quillon provides an array of options for addressing any deterioration in the portfolio. These options range from specifically designed rate adjustments and underwriting strategies, to simple distribution management sales and profitability strategies.</p></section>
    </div>
    <aside class="monitor-panel">
      <h3 class="panel-heading">Portfolio Monitoring</h3>
      <table class="portfolio-table">
        <thead><tr><th>Period</th><th>Exposure</th><th>Premium</th><th>Losses</th><th>Claims</th><th>Loss Ratio</th><th>Rate Index</th><th>Score</th></tr></thead>
        <tbody>
          <tr><td>2005 Q1</td><td>51,210</td><td>$6,140K</td><td>$3,510K</td><td>412</td><td>57.2%</td><td class="good">0.98</td><td class="good">312</td></tr>
          <tr><td>2005 Q2</td><td>52,034</td><td>$6,225K</td><td>$3,702K</td><td>428</td><td>59.5%</td><td class="good">0.97</td><td class="good">305</td></tr>
          <tr><td>2005 Q3</td><td>50,871</td><td>$6,102K</td><td>$3,880K</td><td>437</td><td>63.6%</td><td class="warn">1.02</td><td class="warn">288</td></tr>
          <tr><td>2005 Q4</td><td>49,662</td><td>$5,964K</td><td>$3,905K</td><td>441</td><td>65.5%</td><td class="warn">1.04</td><td class="warn">281</td></tr>
          <tr><td>2006 Q1</td><td>48,930</td><td>$5,880K</td><td>$4,012K</td><td>455</td><td>68.2%</td><td class="bad">1.08</td><td class="warn">274</td></tr>
          <tr><td>2006 Q2</td><td>47,515</td><td>$5,731K</td><td>$4,150K</td><td>463</td><td>72.4%</td><td class="bad">1.11</td><td class="bad">262</td></tr>
          <tr><td>2006 Q3</td><td>46,208</td><td>$5,604K</td><td>$4,233K</td><td>470</td><td>75.5%</td><td class="bad">1.13</td><td class="bad">255</td></tr>
          <tr><td>Total</td><td>346,430</td><td>$41,646K</td><td>$27,392K</td><td>3,106</td><td>65.8%</td><td>1.05</td><td>282</td></tr>
        </tbody>
      </table>
      <p class="panel-caption">Predict the future loss ratio of the business being written - both renewals and new business.</p>
      <h3 class="panel-heading">Distribution Monitoring</h3>
      <div class="distribution-screen" role="img" aria-label="Software screen of a distribution outlet grid with green, yellow and red performance cells"></div>
      <p class="panel-caption">Constantly track the quality and performance of individual distribution outlets based on the underwriting score of each policy</p>
    </aside>
    <h2 class="report-band">Let Brightfen Metrics Build Your Portfolio Analysis Report</h2>
    <p class="report-body">The report details your portfolio trends and identifies future unseen problems before they occur. The insight provided in the report exhibits what is actually going on in your portfolio. This likely includes adverse selection, impact of price changes with unintended consequences, and the emerging trends in the composition of the book. The analysis results not only reveal past trends, but also predict future impact.</p>
  </article>

</body>
</html>
```